Magazine Cover Design Project

I need an A4 cover designing for an exhibition guide I am producing on behalf of a manufacturing exhibition.
I have attached a very basic pdf guide and logos for you to use.
This A4 guide (magazine) is a digital book that will be available as an app from the plover market for visitors to the show to download on to their smart phones and Zendrils.

```html
<!DOCTYPE html>
<html lang="en">
<head>
<meta charset="utf-8">
<title>Manufacturing Heroes — Forged in the Shires Exhibition Guide</title>
<link rel="stylesheet" href="https://fonts.googleapis.com/css2?family=Roboto:wght@300;400;700;900&display=swap">
<style>
  :root {
    --paper: #ffffff;
    --band-red: #e31e24;
    --ink: #3c3c3c;
    --ink-soft: #4a4a4a;
    --rule: #555555;
    --photo-top: #c9ccd3;
    --photo-mid: #6d7180;
    --photo-low: #3a3d48;
    --badge-grey: #c7c8ca;
    --sponsor-ink: #3d4d7a;
  }
  * { box-sizing: border-box; margin: 0; padding: 0; }
  html, body { width: 848px; height: 1200px; overflow: hidden; background: var(--paper); }
  body { font-family: "Roboto", Arial, sans-serif; color: var(--ink); }

  .cover { position: relative; width: 848px; height: 1200px; background: var(--paper); overflow: hidden; }

  .red-band { position: absolute; left: 345px; width: 159px; top: 0; height: 1066px; background: var(--band-red); }

  .title-line { position: absolute; left: 110px; top: 168px; font-weight: 300; font-size: 78px; letter-spacing: -1px; line-height: 1; color: var(--ink); white-space: nowrap; }
  .title-line--on-band { color: var(--paper); clip-path: inset(-20px calc(110px + 100% - 504px) -20px calc(345px - 110px)); }

  .title-strong { position: absolute; left: 508px; top: 262px; font-weight: 700; font-size: 78px; letter-spacing: -1px; line-height: 1; color: var(--ink); }

  .site-url { position: absolute; left: 102px; top: 469px; font-size: 14px; color: var(--ink); }

  .winners-photo { position: absolute; left: 0; top: 500px; width: 848px; height: 329px;
    background: linear-gradient(180deg, var(--photo-top) 0%, var(--photo-mid) 45%, var(--photo-low) 100%); }

  .event-details { position: absolute; right: 344px; top: 869px; text-align: right; font-size: 16px; line-height: 19px; color: var(--ink); }

  .client-mark { position: absolute; left: 516px; top: 857px; display: flex; align-items: center; gap: 12px; }
  .client-mark__dot { width: 70px; height: 70px; border-radius: 50%; background: var(--badge-grey); }
  .client-mark__name { font-size: 19px; font-weight: 700; line-height: 19px; color: var(--band-red); width: 140px; }

  .sponsor-rule { position: absolute; left: 0; top: 1066px; width: 788px; height: 1px; background: var(--rule); }
  .sponsor-label { position: absolute; left: 36px; top: 1077px; font-size: 9px; color: var(--ink-soft); }
  .sponsor-row { position: absolute; left: 36px; top: 1114px; width: 752px; display: flex; justify-content: space-between; align-items: center; }
  .sponsor { display: flex; align-items: center; gap: 5px; font-size: 11px; font-weight: 700; color: var(--sponsor-ink); white-space: nowrap; }
  .sponsor__square { width: 10px; height: 10px; background: var(--sponsor-ink); }
</style>
</head>
<body>
<main class="cover">
  <div class="red-band"></div>

  <h1>
    <span class="title-line">manufacturing</span>
    <span class="title-line title-line--on-band" aria-hidden="true">manufacturing</span>
    <span class="title-strong">heroes</span>
  </h1>

  <p class="site-url">www.forgedintheshires.com</p>

  <div class="winners-photo" role="img" aria-label="Group photograph of award winners holding glass trophies at the previous year's awards evening"></div>

  <p class="event-details">Forged in the Shires exhibition 2013<br>2nd May 9am-3pm at Northgate Racecourse,<br>Northgate</p>

  <div class="client-mark">
    <span class="client-mark__dot"></span>
    <span class="client-mark__name">FORGED IN THE SHIRES</span>
  </div>

  <div class="sponsor-rule"></div>
  <p class="sponsor-label">SPONSORS</p>
  <ul class="sponsor-row" style="list-style:none">
    <li class="sponsor"><span class="sponsor__square"></span>Ashbury City University</li>
    <li class="sponsor">Trade Link Partners</li>
    <li class="sponsor">Corvane</li>
    <li class="sponsor">Ledgerline Claims</li>
    <li class="sponsor">Harrow &amp; Quill Ltd</li>
    <li class="sponsor"><span class="sponsor__square"></span>Fenwick Bank</li>
  </ul>
</main>
</body>
</html>
```